Real Estate Investing company needs a business card design

We need a business card design for new Real Estate Investment Company called "Brightgate Holdings, LLC." We buy homes for cash and close quickly in any situation. Our company provides an easy and fast option for home owners who are in tough situations who need to sell their home fast and don't want realtor fees or other listing hassles. We also renovate and resell our homes which helps provide housing for the community. We would like to see designs that use the colors blue and white to match our company logo or other colors that may match our company logo. The final design should communicate trust and easy process.
Industry/Entity Type
Business
Contact Information for Business Card
Front should have company name and company logo. back of card should have company logo and area to list services.
Look and feel

```html
<!DOCTYPE html>
<html lang="en">
<head>
<meta charset="utf-8">
<title>Brightgate Holdings, LLC — Business Card</title>
<link href="https://fonts.googleapis.com/css2?family=Open+Sans:wght@400;600;700;800&display=swap" rel="stylesheet">
<style>
  :root {
    --bg: #3a3a3c;
    --card: #1e2023;
    --blue: #1a73c9;
    --white: #f2f2f2;
    --muted: #c9c9c9;
  }
  * { margin: 0; padding: 0; box-sizing: border-box; }
  html, body { width: 1200px; height: 1189px; overflow: hidden; }
  body {
    background: var(--bg);
    font-family: "Open Sans", Verdana, sans-serif;
    position: relative;
  }
  .card {
    position: absolute;
    left: 150px;
    width: 900px;
    height: 514px;
    background: var(--card);
    border-radius: 34px;
    box-shadow: 0 18px 40px rgba(0,0,0,0.45);
  }
  .card--services { top: 48px; }
  .card--contact { top: 626px; }

  .brand {
    position: absolute;
    display: flex;
    align-items: center;
    gap: 18px;
    color: var(--blue);
    font-weight: 800;
    text-transform: uppercase;
    line-height: 1.02;
  }
  .brand__mark {
    width: 34px; height: 34px;
    background: var(--blue);
    flex: none;
  }
  .brand__name { font-size: 50px; letter-spacing: 1px; }

  .card--services .brand { left: 170px; top: 96px; }
  .services__title {
    position: absolute;
    left: 470px; top: 250px;
    color: var(--blue);
    font-size: 26px;
    letter-spacing: 1px;
  }
  .services__list {
    position: absolute;
    left: 80px; right: 80px; top: 312px;
    list-style: none;
    color: var(--white);
    font-size: 22px;
    letter-spacing: 2px;
    line-height: 44px;
    text-align: center;
  }

  .card--contact .brand { left: 70px; top: 200px; }
  .card--contact .brand__name { font-size: 40px; }
  .divider {
    position: absolute;
    left: 470px; top: 70px;
    width: 2px; height: 360px;
    background: var(--muted);
  }
  .contact {
    position: absolute;
    left: 510px; top: 92px;
    font-size: 21px;
    line-height: 1.3;
  }
  .contact__name { color: var(--blue); font-weight: 800; font-size: 27px; text-transform: uppercase; }
  .contact__role { color: var(--white); font-weight: 700; font-size: 20px; margin-bottom: 26px; }
  .contact__address { color: var(--blue); margin-bottom: 14px; }
  .contact__row { display: flex; align-items: center; gap: 12px; color: var(--blue); margin-bottom: 4px; }
  .contact__icon {
    width: 28px; height: 28px; flex: none;
    background: var(--white); border-radius: 6px;
  }
  .contact__web { color: var(--white); margin-top: 22px; font-size: 22px; }
</style>
</head>
<body>
  <section class="card card--services">
    <div class="brand">
      <span class="brand__mark"></span>
      <span class="brand__name">Brightgate<br>Holdings</span>
    </div>
    <h2 class="services__title">SERVICES</h2>
    <ul class="services__list">
      <li>xxxxxxx xx xxxx xxx xxxx | xxxx xxx x xxxxx xxxxx xxxxxxxx</li>
      <li>xxxxxxx &amp; xxxxx xxxxxx | xxxxx &amp; xxxxxxxxx xxxxxxx</li>
      <li>xxxxxxx xx xxxx xxx xxxx | xxxx xxx x xxxxx xxxxx xxxxxxxx</li>
    </ul>
  </section>

  <section class="card card--contact">
    <div class="brand">
      <span class="brand__mark"></span>
      <span class="brand__name">Brightgate<br>Holdings</span>
    </div>
    <div class="divider"></div>
    <div class="contact">
      <p class="contact__name">Employee Name</p>
      <p class="contact__role">Director</p>
      <p class="contact__address">0000 your address Avenue<br>Maple Ridge, SD 0000</p>
      <p class="contact__row">
        <svg class="contact__icon" viewBox="0 0 28 28" aria-hidden="true"><rect width="28" height="28" rx="6" fill="#f2f2f2"/><path d="M9 7c1 0 2 3 2 4s-2 1-1 3 3 4 4 4 2-2 3-1 4 2 4 3-2 3-4 3C11 23 5 16 5 11c0-2 2-4 4-4z" fill="#1e2023"/></svg>
        000-000-0000</p>
      <p class="contact__row">
        <svg class="contact__icon" viewBox="0 0 28 28" aria-hidden="true"><rect width="28" height="28" rx="6" fill="#f2f2f2"/><rect x="9" y="5" width="10" height="6" fill="#1e2023"/><rect x="5" y="11" width="18" height="9" rx="2" fill="#1e2023"/><rect x="9" y="17" width="10" height="6" fill="#1e2023"/></svg>
        000-000-0000</p>
      <p class="contact__row">
        <svg class="contact__icon" viewBox="0 0 28 28" aria-hidden="true"><rect width="28" height="28" rx="6" fill="#f2f2f2"/><rect x="5" y="8" width="18" height="12" fill="none" stroke="#1e2023" stroke-width="2"/><path d="M5 8l9 7 9-7" fill="none" stroke="#1e2023" stroke-width="2"/></svg>
        your@yourmail.com</p>
      <p class="contact__web">www.yourwebsite.com</p>
    </div>
  </section>
</body>
</html>
```